Business Cards for Communications Technology Company

We are an innovative software company based in Tropical North Queensland, Australia. We have several brands with a focus on communications software for businesses. We are looking for a business card that is very innovate and creative whilst still remaining professional on a corporate level.

Our internal culture is very progressive and expresses a blend between the clarity of our natural surroundings and the highly technological industry we work in. Our current branding blends a modern minimalist typeface with the desire to push the boundaries in the way we communicate.

This is a corporate level business card for the communications software industry and may possibly also encompass our brands MarNetwork, PelFax, TukMailer and our B2B marketing service—with our companies name being Viresca Partners. Showing other brands on the business card is optional not compulsory.

Technical notes:

-We will attach all logo's and some examples of our corporate branding
- Would be willing to print with various papers, embossed, metallic ink, curved edges etc. in a standard business card size

Sample content:

Rowan Pellick
Senior Account Manager
Phone: 1300 842 916 / +617 4583 2764
Email: r.pellick@viresca.com.au
Web: www.viresca.com.au

Sincerely,
Viresca Partners.

```html
<!DOCTYPE html>
<html lang="en">
<head>
<meta charset="utf-8">
<title>Viresca Partners — Business Card</title>
<link rel="stylesheet" href="https://fonts.googleapis.com/css2?family=Source+Sans+3:wght@400;600;700&display=swap">
<style>
  :root {
    --backdrop: #2a2a2a;
    --metal-light: #f4f4f4;
    --metal-mid: #dedede;
    --metal-dark: #bdbdbd;
    --ink: #3a3a3a;
    --ink-soft: #4a4a4a;
    --accent: #5b8a2e;
    --divider: #9a9a9a;
  }
  * { margin: 0; padding: 0; box-sizing: border-box; }
  html, body {
    width: 1200px; height: 960px; overflow: hidden;
    background: var(--backdrop);
    font-family: "Source Sans 3", "Helvetica Neue", Arial, sans-serif;
  }
  .canvas { position: relative; width: 1200px; height: 960px; }
  .card {
    position: absolute; width: 598px; height: 342px;
    background: linear-gradient(180deg, var(--metal-mid) 0%, var(--metal-light) 30%, var(--metal-light) 65%, var(--metal-dark) 100%);
  }
  .card--front { left: 315px; top: 113px; }
  .card--back { left: 311px; top: 472px; }

  .brand {
    position: absolute; left: 0; right: 0;
    display: flex; align-items: center; justify-content: center; gap: 14px;
  }
  .card--front .brand { top: 78px; }
  .card--back .brand { top: 138px; }
  .brand__mark {
    width: 54px; height: 54px; border-radius: 50%;
    background: var(--accent);
  }
  .brand__name {
    font-size: 58px; font-weight: 400; letter-spacing: 2px;
    color: var(--ink); line-height: 1;
  }

  .identity {
    position: absolute; right: 323px; top: 204px; text-align: right;
  }
  .identity__name {
    font-size: 19px; font-weight: 700; color: var(--accent);
    letter-spacing: 0.3px; line-height: 22px;
  }
  .identity__role {
    font-size: 17px; font-weight: 400; color: var(--ink-soft); line-height: 22px;
  }
  .divider {
    position: absolute; left: 292px; top: 187px; width: 1px; height: 80px;
    background: var(--divider);
  }
  .contact {
    position: absolute; left: 310px; top: 189px; list-style: none;
  }
  .contact__item {
    display: flex; align-items: center; gap: 9px;
    font-size: 15px; color: var(--ink-soft); line-height: 19px;
  }
  .contact__icon { width: 13px; height: 13px; fill: var(--accent); flex: none; }

  .web-line {
    position: absolute; left: 0; right: 0; top: 288px; text-align: center;
    font-size: 15px; letter-spacing: 9px; color: var(--ink); font-weight: 600;
  }
</style>
</head>
<body>
<div class="canvas">
  <section class="card card--front" aria-label="Business card front">
    <div class="brand">
      <span class="brand__mark"></span>
      <span class="brand__name">VIRESCA</span>
    </div>
    <div class="identity">
      <p class="identity__name">ROWAN PELLICK</p>
      <p class="identity__role">Senior Account Manager</p>
    </div>
    <span class="divider"></span>
    <ul class="contact">
      <li class="contact__item">
        <svg class="contact__icon" viewBox="0 0 13 13"><path d="M1 4 Q6.5 0 12 4 L10 5.5 L8.5 4 L4.5 4 L3 5.5 Z M3 7 H10 L11 12 H2 Z"/></svg>
        1300 842 916
      </li>
      <li class="contact__item">
        <svg class="contact__icon" viewBox="0 0 13 13"><path d="M1 4 Q6.5 0 12 4 L10 5.5 L8.5 4 L4.5 4 L3 5.5 Z M3 7 H10 L11 12 H2 Z"/></svg>
        +617 4583 2764
      </li>
      <li class="contact__item">
        <svg class="contact__icon" viewBox="0 0 13 13"><path d="M1 3 H12 V11 H1 Z" /><path d="M1 3 L6.5 7.5 L12 3" fill="none" stroke="#f2f2f2" stroke-width="1.2"/></svg>
        r.pellick@viresca.com.au
      </li>
      <li class="contact__item">
        <svg class="contact__icon" viewBox="0 0 13 13"><circle cx="6.5" cy="6.5" r="5.5"/><path d="M1 6.5 H12 M6.5 1 Q3 6.5 6.5 12 Q10 6.5 6.5 1" fill="none" stroke="#f2f2f2" stroke-width="0.9"/></svg>
        www.viresca.com.au
      </li>
    </ul>
  </section>

  <section class="card card--back" aria-label="Business card back">
    <div class="brand">
      <span class="brand__mark"></span>
      <span class="brand__name">VIRESCA</span>
    </div>
    <p class="web-line">www.viresca.com.au</p>
  </section>
</div>
</body>
</html>
```